Dialysis Brochure

12 pages booklet, horizontal, 9 inches width x 6 inches high , luxury look
Updates

Landscape booklet 9 x 6

Need extra days to review

Target Market(s)

General public

Industry/Entity Type

Health Care

Colors

Designer to choose colors to be used in the design.

Requirements
Nice to have
• foil effect or similar

```html
<!DOCTYPE html>
<html lang="en">
<head>
<meta charset="utf-8">
<title>Dialysis Brochure – Doctor's Services Spread</title>
<link href="https://fonts.googleapis.com/css2?family=Source+Sans+3:wght@300;400;500&display=swap" rel="stylesheet">
<style>
  :root {
    --paper: #e6e5e3;
    --band: #574b41;
    --band-veil: rgba(96, 83, 72, 0.86);
    --text-light: #f6f3ee;
    --title: #4a4440;
    --ceiling: #f1f2f2;
    --wall: #c9cdcf;
    --wood: #b27d4b;
    --wood-light: #c89a6a;
    --floor: #8e9193;
    --floor-dark: #76797b;
  }
  * { margin: 0; padding: 0; box-sizing: border-box; }
  html, body { width: 1200px; height: 400px; overflow: hidden; background: var(--paper); }
  body { font-family: "Source Sans 3", "Source Sans Pro", sans-serif; }

  .spread { position: relative; width: 1200px; height: 400px; background: var(--paper); overflow: hidden; }

  .hero-photo {
    position: absolute; left: 0; top: 0; width: 844px; height: 400px;
    background:
      linear-gradient(90deg, rgba(0,0,0,0) 0%, rgba(0,0,0,0) 55%, rgba(110,114,116,0.35) 100%),
      linear-gradient(180deg, var(--ceiling) 0%, #e4e6e7 22%, var(--wall) 36%, var(--wood) 48%, var(--wood-light) 60%, #d9cfc4 70%, var(--floor) 86%, var(--floor-dark) 100%);
  }

  .schedule-band {
    position: absolute; left: 0; top: 267px; width: 513px; height: 75px;
    background: var(--band-veil);
  }
  .schedule-list {
    position: absolute; left: 335px; top: 276px; width: 180px;
    list-style: none; color: var(--text-light);
    font-size: 7.6px; line-height: 13px; font-weight: 400; white-space: nowrap;
  }

  .services-title {
    position: absolute; left: 900px; top: 62px;
    font-weight: 300; font-size: 22.5px; letter-spacing: 2.9px;
    color: var(--title); white-space: nowrap;
  }
  .services-band {
    position: absolute; left: 902px; top: 98px; width: 298px; height: 61px;
    background: var(--band);
  }
  .services-list {
    position: absolute; left: 909px; top: 102px; width: 288px;
    list-style: none; color: var(--text-light);
    font-size: 7.5px; line-height: 13px; font-weight: 400; white-space: nowrap;
  }

  .bullet-list li { position: relative; padding-left: 8px; }
  .bullet-list li::before { content: "•"; position: absolute; left: 0; }
  .bullet-list li.continued::before { content: ""; }

  .care-photo {
    position: absolute; left: 902px; top: 182px; width: 239px; height: 159px;
    background: linear-gradient(180deg, #eceeef 0%, #d3d7d9 38%, #a9896b 62%, #6f7f9c 80%, #8a8078 100%);
  }
</style>
</head>
<body>
  <main class="spread">
    <div class="hero-photo" role="img" aria-label="Bright dialysis treatment floor with wood-panelled nurse stations, reclining treatment chairs and dialysis machines"></div>

    <div class="schedule-band"></div>
    <ul class="schedule-list bullet-list">
      <li>Regular shifts (Monday/ Wednesday/ Friday or</li>
      <li class="continued">Tuesday/ Thursday/ Saturday)</li>
      <li>Early Morning shifts (as early as 5AM)</li>
      <li>Late Afternoon Shifts (after 5PM)</li>
    </ul>

    <h1 class="services-title">Doctor’s Services</h1>
    <div class="services-band"></div>
    <ul class="services-list bullet-list">
      <li>Full-time Nephrology staff physician on premises</li>
      <li>11 Board Certified Nephrologists</li>
      <li>orYOU MAY KEEP YOUR CURRENT NEPHROLOGIST</li>
      <li class="continued">when you transfer to our Center</li>
    </ul>

    <div class="care-photo" role="img" aria-label="Care team attending to a patient seated in a dialysis chair beside a dialysis machine"></div>
  </main>
</body>
</html>
```